Lernoptic.com Business Card Design Project

We need a new business card design for our new online company that delivers online education. It initially focused on SEO training but will soon offer more. The design should be fresh and trendy and take into account the colors and website design attached.
Industry/Entity Type
Training

```html
<!DOCTYPE html>
<html lang="en">
<head>
<meta charset="utf-8">
<title>Lernoptic Business Card</title>
<link rel="stylesheet" href="https://fonts.googleapis.com/css2?family=Arimo:wght@400&display=swap">
<style>
  :root {
    --brand-green: #0a7f45;
    --text-gray: #6d6e70;
    --card-white: #ffffff;
    --frame-black: #000000;
  }
  * { margin: 0; padding: 0; box-sizing: border-box; }
  html, body {
    width: 1200px;
    height: 687px;
    overflow: hidden;
    background: var(--card-white);
  }
  .card {
    position: relative;
    width: 1200px;
    height: 687px;
    background: var(--card-white);
    border: 3px solid var(--frame-black);
    font-family: "Arimo", Arial, sans-serif;
    overflow: hidden;
  }
  .corner-band {
    position: absolute;
    left: 0;
    top: 0;
    width: 417px;
    height: 343px;
  }
  .brand {
    position: absolute;
    right: 66px;
    top: 66px;
    display: flex;
    align-items: center;
    gap: 26px;
  }
  .brand-dot {
    width: 112px;
    height: 112px;
    border-radius: 50%;
    background: var(--brand-green);
  }
  .brand-name {
    font-size: 112px;
    line-height: 1;
    color: var(--text-gray);
    font-weight: 400;
    letter-spacing: -1px;
  }
  .contact {
    position: absolute;
    right: 110px;
    top: 308px;
    text-align: right;
    color: var(--text-gray);
    line-height: 1;
  }
  .contact-name {
    font-size: 66px;
    color: var(--brand-green);
    letter-spacing: -0.5px;
  }
  .contact-role {
    font-size: 23px;
    margin-top: 3px;
  }
  .contact-phone {
    font-size: 40px;
    margin-top: 20px;
  }
  .contact-email {
    font-size: 40px;
    margin-top: 17px;
  }
  .footer-line {
    position: absolute;
    left: 139px;
    top: 643px;
    display: flex;
    gap: 17px;
    font-size: 24px;
    line-height: 1;
    color: var(--text-gray);
  }
</style>
</head>
<body>
  <div class="card">
    <svg class="corner-band" viewBox="0 0 417 343" aria-hidden="true">
      <polygon points="0,0 417,0 0,343" fill="var(--brand-green)"/>
    </svg>

    <div class="brand">
      <span class="brand-dot" aria-hidden="true"></span>
      <span class="brand-name">Lernoptic</span>
    </div>

    <div class="contact">
      <p class="contact-name">Daniel Hart</p>
      <p class="contact-role">Consultant</p>
      <p class="contact-phone">(+253) 555-014-278</p>
      <p class="contact-email">daniel.hart@lernoptic.com</p>
    </div>

    <div class="footer-line">
      <span>Lernoptic info</span>
      <span>Lernoptic info</span>
      <span>Lernoptic info</span>
      <span>Lernoptic info</span>
      <span>Lernoptic info</span>
    </div>
  </div>
</body>
</html>
```